Redesign of page from emergency manual

Please redesign this PDF to look better. Please don't include any stock photos. It must be legible. Making some words bold is probably a good idea.

Here are some things I like :

https://brambolthouse.com.au/collections/frontpage/products/the-kvt-v2-ebook

https://media-qz.fennowstatic.net/kd-pqRwTbnVYy_ZaWsLmHu400K4sa-Xe9vbPqTn37sJdVRwaT4PiedfxrmZ8NTcUjK=w1052-h592-rw

```html
<!DOCTYPE html>
<html lang="en">
<head>
<meta charset="utf-8">
<title>Hypertension, Acute</title>
<link rel="stylesheet" href="https://fonts.googleapis.com/css2?family=Poppins:wght@400;500;600;700;800&display=swap">
<style>
  :root {
    --page-bg: #e3e3e3;
    --card-bg: #ffffff;
    --navy: #0a2a8c;
    --royal: #0d3bb0;
    --accent: #0b2f9e;
    --ink: #111111;
    --panel: #f1f1f1;
    --label-bg: #e6e6e6;
    --rule: #8a8a8a;
    --alert: #e8141b;
  }
  * { box-sizing: border-box; margin: 0; padding: 0; }
  html, body { width: 874px; height: 1200px; overflow: hidden; }
  body {
    background: var(--page-bg);
    font-family: "Poppins", sans-serif;
    color: var(--ink);
    position: relative;
  }
  .sheet {
    position: absolute; left: 42px; top: 41px; width: 789px; height: 1112px;
    background: var(--card-bg);
    box-shadow: 8px 10px 14px rgba(0,0,0,0.22);
  }
  .masthead {
    position: absolute; left: 0; top: 0; width: 100%; height: 76px;
    background: linear-gradient(100deg, var(--navy) 0%, var(--royal) 45%, var(--navy) 100%);
    color: #fff; display: flex; align-items: center; white-space: nowrap;
  }
  .masthead-title { margin-left: 28px; font-size: 30px; font-weight: 800; letter-spacing: -0.2px; }
  .masthead-rule { width: 2px; height: 34px; background: #fff; margin: 0 14px; flex: none; }
  .masthead-sub { font-size: 16.5px; font-weight: 700; line-height: 20px; }

  .checklist { position: absolute; left: 28px; top: 97px; width: 740px; list-style: none; }
  .checklist li { position: relative; padding-left: 30px; font-size: 15.5px; line-height: 18px; margin-bottom: 13px; }
  .checklist li svg { position: absolute; left: 0; top: 4px; width: 16px; height: 14px; }
  .checklist .hl { color: var(--accent); font-weight: 700; }
  .checklist .note { display: block; font-size: 13px; margin-top: 6px; margin-left: -1px; }

  .bp-table {
    position: absolute; left: 36px; top: 238px; width: 716px;
    border: 1px solid var(--navy); border-collapse: collapse; table-layout: fixed;
  }
  .bp-table td { text-align: center; font-size: 16px; font-weight: 500; border-left: 1px solid var(--navy); height: 40px; }
  .bp-table .bp-head td { background: var(--panel); color: var(--navy); font-weight: 700; height: 47px; }
  .bp-table .bp-row td { border-top: 1px dashed var(--rule); }
  .bp-table .bp-row td.bp-label { border-top: none; }
  .bp-table .bp-label {
    background: var(--label-bg); color: var(--navy); font-weight: 700;
    font-size: 16.5px; line-height: 27.5px; text-align: right; padding: 30px 28px 0 0;
    border-left: none; vertical-align: top;
  }
  .bp-table .bp-label span { display: block; }
  .bp-table .bp-label span:last-child { margin-right: -4px; }

  .caution { position: absolute; left: 36px; top: 422px; width: 716px; }
  .caution svg { position: absolute; left: 0; top: 24px; width: 52px; height: 46px; }
  .caution-body { margin-left: 59px; }
  .caution h3 { font-size: 16.5px; font-weight: 800; line-height: 22px; }
  .caution p { font-size: 14.3px; line-height: 17.5px; text-align: justify; }

  .drug-table { position: absolute; left: 0; top: 522px; width: 789px; border-collapse: collapse; }
  .drug-table thead th {
    height: 36px; color: #fff; font-size: 17px; font-weight: 700;
    background: linear-gradient(100deg, var(--navy), var(--royal) 50%, var(--navy));
  }
  .drug-table .col-action { width: 340px; text-align: right; padding-right: 36px; padding-top: 4px; }
  .drug-table .col-drug { text-align: left; padding-left: 21px; border-left: 2px solid #fff; }
  .drug-table td { border-top: 1px dashed var(--rule); }
  .drug-table tbody tr:first-child td { border-top: none; }
  .drug-table .action {
    background: var(--panel); text-align: right; padding-right: 42px;
    font-size: 14px; font-weight: 500; letter-spacing: 0.2px; border-right: 1px solid var(--rule);
  }
  .drug-table .drugs { padding-left: 20px; font-size: 15px; line-height: 17.5px; }
  .drug-table .drugs div + div { margin-top: 6px; }
  .drug-table .drugs .indent { padding-left: 14px; }
  .drug-table .dose { color: var(--accent); font-weight: 600; }
  .drug-table .bold { font-weight: 700; }

  .differential-tag {
    position: absolute; left: 225px; top: 876px; width: 312px; height: 36px;
    background: var(--royal); color: #fff; font-size: 16px; font-weight: 700;
    display: flex; align-items: center; justify-content: center;
  }
  .differential { position: absolute; left: 0; top: 0; width: 100%; }
  .dx { position: absolute; display: flex; align-items: center; font-size: 16.5px; font-weight: 600; white-space: nowrap; }
  .dx-icon { width: 20px; height: 20px; border-radius: 50%; margin-right: 16px; flex: none;
    background: radial-gradient(circle at 40% 40%, #3f6be0, var(--navy)); }
</style>
</head>
<body>
  <main class="sheet">
    <header class="masthead">
      <h1 class="masthead-title">HYPERTENSION, ACUTE</h1>
      <span class="masthead-rule"></span>
      <p class="masthead-sub">Sustained high blood pressure<br>refractory to treating reversible causes</p>
    </header>

    <ul class="checklist">
      <li><svg viewBox="0 0 16 14"><path d="M1 7 L6 12 L15 1" fill="none" stroke="#0d3bb0" stroke-width="2.4"/></svg>In pediatrics, hypertension is almost always treated by addressing likely causes such as light anesthesia or measurement error</li>
      <li><svg viewBox="0 0 16 14"><path d="M1 7 L6 12 L15 1" fill="none" stroke="#0d3bb0" stroke-width="2.4"/></svg>Ensure correct BP cuff size: cuff bladder width <span class="hl">~ 40%</span> of limb circumference</li>
      <li><svg viewBox="0 0 16 14"><path d="M1 7 L6 12 L15 1" fill="none" stroke="#0d3bb0" stroke-width="2.4"/></svg>Ensure arterial line transducer is at level of heart<span class="note">(Consider placing arterial line if not already present )</span></li>
    </ul>

    <table class="bp-table">
      <colgroup>
        <col style="width:178px"><col style="width:177px"><col style="width:187px"><col style="width:174px">
      </colgroup>
      <tbody>
        <tr class="bp-head">
          <td class="bp-label" rowspan="4"><span>HYPERTENSIVE</span><span>BLOOD</span><span>PRESSURE</span><span>RANGE</span></td>
          <td>Age (yr)</td><td>Systolic</td><td>Diastolic</td>
        </tr>
        <tr class="bp-row"><td>Newborn</td><td>&gt;97</td><td>&gt;70</td></tr>
        <tr class="bp-row"><td>1-3</td><td>&gt;105</td><td>&gt;61</td></tr>
        <tr class="bp-row"><td>4-12</td><td>&gt;113</td><td>&gt;86</td></tr>
      </tbody>
    </table>

    <section class="caution">
      <svg viewBox="0 0 52 46" aria-hidden="true"><path d="M26 3 Q28 1 30 4 L50 40 Q51 44 47 44 L5 44 Q1 44 2 40 L22 4 Q24 1 26 3Z" fill="#e8141b"/><rect x="24" y="13" width="4.5" height="18" rx="2" fill="#fff"/><circle cx="26.2" cy="37" r="2.7" fill="#fff"/></svg>
      <div class="caution-body">
        <h3>CAUTION:</h3>
        <p>Anti-hypertensive drugs are almost never needed for routine pediatric cases. These medi-cations are used almost exclusively for specialized cardiac, neurosurgical, or endocrine (pheochromocytoma) cases. Consult an expert before use. Rule-out increased ICP.</p>
      </div>
    </section>

    <table class="drug-table">
      <thead>
        <tr><th class="col-action">ACTION</th><th class="col-drug">DRUG (IV DOSING)</th></tr>
      </thead>
      <tbody>
        <tr style="height:65px">
          <td class="action">DIRECT SMOOTH MUSCLE RELAXATION</td>
          <td class="drugs">
            <div>- Sodium nitroprusside <span class="dose">0.5-10</span> MICROgrams/kg/min</div>
            <div>- HydrALAZINE <span class="dose">0.1-0.2 mg/kg</span> (adult dose <span class="dose">5-10 mg</span>)</div>
          </td>
        </tr>
        <tr style="height:106px">
          <td class="action"><span class="bold">B-</span>ADRENERGIC BLOCKADE</td>
          <td class="drugs">
            <div>- Esmolol <span class="dose">100-500</span> MICROgrams/kg over 5 min,<br><span class="indent">then <span class="dose">25-300</span> MICROgrams/kg/min</span></div>
            <div>- Labetalol (also a effect) <span class="dose">0.2-1 mg/kg</span> q 10 min;<br><span class="indent" style="padding-left:10px"><span class="dose">0.4-3</span> mg/kg/hour (infusion)</span></div>
          </td>
        </tr>
        <tr style="height:71px">
          <td class="action">CALCIUM CHANNEL BLOCKADE</td>
          <td class="drugs">
            <div>- BiCARdapine <span class="dose">0.5-5</span> MICROgrams/kg/min</div>
            <div>- Clevidipine <span class="dose">0.5-3.5</span> MICROgrams/kg/min</div>
          </td>
        </tr>
        <tr style="height:46px">
          <td class="action">D1-DOPAMINE AGONIST</td>
          <td class="drugs"><div>- Fenoldopam <span class="dose">0.2-0.8</span> MICROgrams/kg/min</div></td>
        </tr>
      </tbody>
    </table>

    <div class="differential-tag">CONSIDER DIFFERENTIAL (PARTIAL)</div>
    <section class="differential">
      <div class="dx" style="left:38px;top:927px"><span class="dx-icon" role="img" aria-label="Anesthesia icon"></span>Light anesthesia (consider vaporizer or infusion pump empty or malfunctioning)</div>
      <div class="dx" style="left:38px;top:965px"><span class="dx-icon" role="img" aria-label="Heart monitor icon"></span>Arterial line transducer too low or BP cuff too small</div>
      <div class="dx" style="left:38px;top:1001px"><span class="dx-icon" role="img" aria-label="CO2 molecule icon"></span>Hypercarbia</div>
      <div class="dx" style="left:265px;top:1001px"><span class="dx-icon" role="img" aria-label="Oxygen drop icon"></span>Hypoxemia</div>
      <div class="dx" style="left:450px;top:1001px"><span class="dx-icon" role="img" aria-label="Syringe icon"></span>Withdrawal (EtOH or opioid)</div>
      <div class="dx" style="left:38px;top:1048px"><span class="dx-icon" role="img" aria-label="Thyroid icon"></span>Thyroid Storm</div>
      <div class="dx" style="left:265px;top:1048px"><span class="dx-icon" role="img" aria-label="Alert icon"></span>Drug Error</div>
      <div class="dx" style="left:450px;top:1048px"><span class="dx-icon" role="img" aria-label="Adrenal gland icon"></span>Pheochromocytoma</div>
    </section>
  </main>
</body>
</html>
```